依頼概要
【イベント概要】
栃木県北陽市で行われる、「星と風のカーニバル」という冬のイルミネーションイベントです。
実施期間中は、地元中学校吹奏楽部による演奏や各種イベントを行う予定です。

■依頼の内容
イルミネーションのイベントと分かるデザインの作製をお願いいたします。(A2サイズ)
ご参考までに昨年度事務局にて作成いたしましたポスターをご確認ください。

【希望デザイン】
・添付しました背景用写真をベースに他素材用写真を昨年度のように飾りとして配置いただきたいです。(使用する写真の枚数や文字の配置場所の指定はございません。)

■ 納品ファイルの希望
イラストレーター形式/PDF形式データの両方

【入れて欲しい文言】
Star and wind carnival 2019
星と風のカーニバル2019
北陽電鉄「南久保田駅」東口周辺
2019年12月2日(月)~2020年1月13日(月)
点灯時間:17:00~23・00

北陽南久保田駅東口周辺&モールかみさとイベント

■かみさとぬくもり広場 12月1日(日) 10:00~16:00
(星と風のカーニバルプレイベント)
会場:モールかみさと交流サロン
・地ビール 浩三郎日記「穂蔵」・大平巨峰ワイン2019新酒 試飲販売
・森田早苗・川村静江 ピアノデュオ 13:30~
・内藤朋香 CDコンサート
松永里沙(ふるさと希望親善員)キャラクター展 同時開催

■点灯式 12月2日(月)
17:40 点灯式(18:00点灯)
18:15 上郷中学校吹奏楽部演奏
協力:婦人クラブ とん汁無料配布(予定数がなくなり次第終了となります)

■にこにこデッキのもの作り体験 12月15日(日)
スノードーム・キャンドルをつくろう
体験料金:500円(材料費を含む)
会場:モールかみさと内交流サロン
時間:未定
※未就学のお子さんは保護者の方の付き添いをお願いいたします。
体験のご予約・お問い合わせ 0X0-XXXX-XXXX

■モールかみさとクリスマスチャリティイベント(仮)
12月22日(日)
※5行ほど文章の追加があります

■クリスマスイベント 12月23日(月)
16:00 北原園芸高校による模擬店(パン・野菜など)
16:30 ピアノ&ドラムデュオバンド 雪灯-yukiakari-
17:00 上郷さくら保育園お遊戯

お問い合わせ モールかみさと TEL. 0555-71-2946
主催:星と風のカーニバル実行委員会 共催:北陽市
事務局:北陽市上郷地域活性課 商工観光係 TEL.0555-71-5830

(※)
イベント内容については、一部変更予定です。
当選候補の方には文章の追加・修正をお願いしたいと思っております。
また、「にこにこデッキのものづくり体験」の横に画像データの挿入を
併せてお願いすることとなります。
その他、ご質問やご不明な点等がございましたら、ご連絡ください。
何卒宜しくお願い致します。
素材画像を追加いたします。併せてご確認ください。
素材写真を再添付いたします。
■ 選んだ理由

イルミネーションを中心とした全体に統一感のあるレイアウトであり非常に見やすく、目の留まりやすいデザインであることから選ばせていただきました。華やかかつ綺麗にまとめていただいたことが選定のポイントでした。

■ 提案者全員のお礼・コメント

この度は、多くのご提案をいただき誠にありがとうございました。
作成いただいたデザインはどれも素晴らしく、選定が非常に難しいものでした。
再度機会がありましたら、どうぞよろしくお願いいたします。

```html
<!DOCTYPE html>
<html lang="ja">
<head>
<meta charset="utf-8">
<title>星と風のカーニバル2019</title>
<link href="https://fonts.googleapis.com/css2?family=Noto+Sans+JP:wght@400;700;900&family=Shippori+Mincho+B1:wght@800&family=Parisienne&display=swap" rel="stylesheet">
<style>
:root{
  --navy:#0b1a3f;
  --navy-deep:#061029;
  --panel:#0f2456;
  --panel-line:#3e5fa8;
  --gold:#f3c866;
  --gold-deep:#c8902c;
  --white:#ffffff;
  --pale:#dbe6ff;
  --head:#1b3c86;
  --tag:#fbe9b4;
}
*{margin:0;padding:0;box-sizing:border-box}
html,body{width:855px;height:1200px;overflow:hidden;background:var(--navy-deep)}
.poster{position:relative;width:855px;height:1200px;overflow:hidden;font-family:"Noto Sans JP",sans-serif;color:var(--white);background:var(--navy)}
.hero-photo{position:absolute;left:0;top:0;width:855px;height:500px;
  background:radial-gradient(ellipse at 30% 60%,#f7d68a 0%,#b27a2e 22%,transparent 50%),
             radial-gradient(ellipse at 80% 70%,#e9c272 0%,#7a5120 25%,transparent 55%),
             linear-gradient(180deg,#06123a 0%,#10245a 50%,#3a2a1a 100%)}
.hero-fade{position:absolute;left:0;top:380px;width:855px;height:130px;background:linear-gradient(180deg,transparent,var(--navy))}
.round-photo{position:absolute;border-radius:50%;border:3px solid var(--gold)}
.round-a{left:14px;top:18px;width:250px;height:250px;background:radial-gradient(circle at 50% 40%,#f2d28c,#6a4a22 60%,#1a1a2a)}
.round-b{left:40px;top:245px;width:180px;height:180px;background:radial-gradient(circle at 50% 50%,#f6e0a0,#a0382c 55%,#2a1a18)}
.title{position:absolute;right:30px;top:14px;width:560px;text-align:center;font-family:"Shippori Mincho B1",serif;font-weight:800;color:var(--white);-webkit-text-stroke:3px var(--gold-deep);paint-order:stroke fill;text-shadow:0 0 14px rgba(255,220,140,.8)}
.title .l1{display:block;font-size:104px;line-height:1.05}
.title .l2{display:block;font-size:86px;line-height:1.1}
.subtitle{position:absolute;right:40px;top:222px;width:520px;text-align:center;font-family:"Parisienne",cursive;font-size:34px;color:var(--pale)}
.dates{position:absolute;right:30px;top:332px;width:560px;text-align:center}
.dates .range{font-size:60px;font-weight:900;color:var(--gold);letter-spacing:1px;line-height:1}
.dates .range small{font-size:30px}
.dates .hours{font-size:30px;font-weight:700;margin-top:8px}
.dates .place{font-size:26px;font-weight:700;margin-top:2px}
.section-head{position:absolute;left:30px;top:508px;width:795px;height:40px;border-top:2px solid var(--gold);border-bottom:2px solid var(--gold);text-align:center;font-size:21px;font-weight:900;line-height:36px;color:var(--gold)}
.col{position:absolute;top:566px;width:385px;display:flex;flex-direction:column;gap:14px}
.col-left{left:30px}
.col-right{left:440px}
.event{background:var(--panel);border:1px solid var(--panel-line)}
.event-head{display:flex;align-items:center;height:34px;background:var(--head)}
.event-date{background:var(--tag);color:var(--navy);font-weight:900;font-size:16px;padding:0 12px;height:34px;line-height:34px;flex:none}
.event-name{font-weight:900;font-size:16px;color:var(--gold);padding-left:12px;line-height:1.15}
.event-body{padding:8px 12px 10px;font-size:12px;line-height:1.6;white-space:nowrap}
.event-body .lead{font-weight:700;font-size:13.5px}
.craft-photos{display:flex;gap:8px;margin-top:8px}
.craft-photos div{flex:1;height:78px;border-radius:4px;background:radial-gradient(circle at 50% 45%,#fff4d6,#8fb0d8 55%,#33466e)}
.tall-head{height:44px}
.tall-head .event-date{height:44px;line-height:44px}
.footer{position:absolute;left:0;top:1112px;width:855px;height:88px;background:var(--navy-deep);border-top:2px solid var(--gold);padding:10px 30px;font-size:13px;line-height:1.6;display:grid;grid-template-columns:1fr 1fr}
</style>
</head>
<body>
<div class="poster">
  <div class="hero-photo" role="img" aria-label="イルミネーションに彩られた駅前広場の夜景写真"></div>
  <div class="hero-fade"></div>
  <div class="round-photo round-a" role="img" aria-label="サロンでの演奏会の写真"></div>
  <div class="round-photo round-b" role="img" aria-label="イルミネーション前のサンタクロースの写真"></div>

  <h1 class="title"><span class="l1">星と風の</span><span class="l2">カーニバル</span></h1>
  <p class="subtitle">Star and wind carnival 2019</p>
  <div class="dates">
    <div class="range">12.2<small>[月]</small>~1.13<small>[月]</small></div>
    <div class="hours">点灯時間:17:00~23:00</div>
    <div class="place">北陽電鉄「南久保田駅」東口周辺</div>
  </div>

  <h2 class="section-head">北陽南久保田駅東口周辺&amp;モールかみさとイベント</h2>

  <div class="col col-left">
    <section class="event">
      <div class="event-head"><span class="event-date">12/1(日)</span><span class="event-name">かみさとぬくもり広場</span></div>
      <div class="event-body">
        <p class="lead">星と風のカーニバルプレイベント</p>
        <p>会場:モールかみさと交流サロン</p>
        <p>10:00~ 森田早苗・川村静江 ピアノデュオ</p>
        <p>内藤朋香 CDコンサート</p>
        <p>地ビール 浩三郎日記「穂蔵」・上郷紅玉ワイン</p>
        <p>2019新酒試飲販売</p>
        <p>■松永里沙(ふるさと希望親善員)キャラクター展同時開催</p>
      </div>
    </section>
    <section class="event">
      <div class="event-head"><span class="event-date">12/15(日)</span><span class="event-name">にこにこデッキのもの作り体験</span></div>
      <div class="event-body">
        <p class="lead">スノードーム・キャンドルをつくろう</p>
        <p>会場:モールかみさと内交流サロン</p>
        <p>時間:未定</p>
        <p>体験料金:500円(材料費を含む)</p>
        <p>※未就学のお子さんは保護者の方の付き添いを</p>
        <p>　お願いいたします。</p>
        <p>体験のご予約・お問い合わせ 0X0-XXXX-XXXX</p>
        <div class="craft-photos">
          <div role="img" aria-label="手作りスノードームの写真"></div>
          <div role="img" aria-label="手作りキャンドルの写真"></div>
          <div role="img" aria-label="手作りクリスマス雑貨の写真"></div>
        </div>
      </div>
    </section>
  </div>

  <div class="col col-right">
    <section class="event">
      <div class="event-head"><span class="event-date">12/2(月)</span><span class="event-name">点灯式</span></div>
      <div class="event-body">
        <p>17:40 点灯式(18:00点灯)</p>
        <p>18:15 上郷中学校吹奏楽部演奏</p>
        <p>協力:婦人クラブ とん汁無料配布</p>
        <p>(予定数がなくなり次第終了となります)</p>
      </div>
    </section>
    <section class="event">
      <div class="event-head tall-head"><span class="event-date">12/22(日)</span><span class="event-name">モールかみさとクリスマス<br>チャリティイベント</span></div>
      <div class="event-body">
        <p>テキストテキストテキストテキストテキストテキスト</p>
        <p>テキストテキストテキストテキストテキストテキスト</p>
        <p>テキストテキストテキストテキストテキストテキスト</p>
        <p>テキストテキストテキストテキストテキストテキスト</p>
        <p>テキストテキストテキストテキストテキスト</p>
      </div>
    </section>
    <section class="event">
      <div class="event-head"><span class="event-date">12/23(月)</span><span class="event-name">クリスマスイベント</span></div>
      <div class="event-body">
        <p>16:00 北原園芸高校による模擬店(パン・野菜など)</p>
        <p>16:30 ピアノ&amp;ドラムデュオバンド 雪灯-yukiakari-</p>
        <p>17:00 上郷さくら保育園お遊戯</p>
      </div>
    </section>
  </div>

  <footer class="footer">
    <div>
      <p>お問い合わせ モールかみさと TEL. 0555-71-2946</p>
      <p>主催:星と風のカーニバル実行委員会 共催:北陽市</p>
    </div>
    <div>
      <p>事務局:北陽市上郷地域活性課 商工観光係</p>
      <p>TEL.0555-71-5830</p>
    </div>
  </footer>
</div>
</body>
</html>
```